Business Card for Mortgage Loan Originator

Mortgage Loan Originator

To instantly "identify who I am", "what I do", and attest to my credibility". Basically, why they should do business with me versus your competitor.

The way I explain what I'm better than others in my industry, is "keeping the process simple and easy".

I would like to keep my card simple and easy...something that tells a person about what I do and how I conduct business at a single look of the card or at the VERY VERY least is eye catching.

My business complicated and detailed and I have streamlined it to "Simple and Easy" - which is Modern and Upscale for the way this business was viewed in the past.

Industry/Entity Type

Mortgage

Contact Information for Business Card

I've attached the current business card. For compliance, all of this information MUST be on the card.

The Company website COULD also be included:
www.brightvalehomeloans.com.

Logo's can also be found on the website.

I'm open to upgrading the current design or even a whole NEW logo and design!

Font styles to use
Sans Serif

Colors

Designer to choose colors to be used in the design.

Requirements
Must have
• I've attached the current business card. For compliance, all of this information MUST be on the card.
• The Company website COULD also be included on the back
• www.brightvalehomeloans.com.
• Logo's can also be found on the website.
• I'm open to upgrading the current design or even a whole NEW logo and design!
• Top Producer 2013, 2014, 2015, 2016
Nice to have
• Something nice and up-to-date! The current card is boring and old!
• Instead of a plain white, there could be a design or print in the background.
• On the front or back of the card:
• Licensed in TX, AL, AR, CA, CO, FL, LA, OK
• Keeping the process simple and easy!
Should not have
• not affiliated wit US Government logos or affiliations
• To avoid is that your card is so "forgettable" that it gets dropped in a drawer, forgotten, or worse yet, thrown in the trash!

```html
<!DOCTYPE html>
<html lang="en">
<head>
<meta charset="utf-8">
<title>Reid Calloway – Business Card</title>
<link rel="stylesheet" href="https://fonts.googleapis.com/css2?family=Oswald:wght@500&family=Open+Sans:wght@600;700&display=swap">
<style>
  :root {
    --slate-dark: #1f272e;
    --slate-mid: #2f3a43;
    --slate-light: #46525c;
    --accent-red: #c42a22;
    --accent-red-deep: #8e1b16;
    --accent-blue: #1f3f9c;
    --accent-blue-deep: #17307a;
    --ink-white: #ffffff;
  }
  html, body {
    margin: 0;
    padding: 0;
    width: 1200px;
    height: 666px;
    overflow: hidden;
    background: #ffffff;
  }
  .business-card {
    position: relative;
    width: 1200px;
    height: 666px;
    overflow: hidden;
    color: var(--ink-white);
    font-family: "Open Sans", Arial, sans-serif;
  }
  .card-background {
    position: absolute;
    inset: 0;
    width: 100%;
    height: 100%;
  }
  .identity {
    position: absolute;
    left: 64px;
    top: 56px;
  }
  .identity__name {
    margin: 0;
    font-family: "Oswald", "Arial Narrow", sans-serif;
    font-weight: 500;
    font-size: 84px;
    line-height: 1;
    letter-spacing: 1px;
    text-transform: uppercase;
  }
  .identity__credentials {
    margin: 14px 0 0;
    font-size: 16px;
    font-weight: 600;
    line-height: 23px;
  }
  .identity__promise {
    margin: 30px 0 0;
    font-size: 21px;
    font-weight: 700;
    line-height: 27px;
  }
  .contact-list {
    position: absolute;
    left: 668px;
    top: 326px;
    margin: 0;
    padding: 0;
    list-style: none;
    font-size: 19px;
    font-weight: 700;
  }
  .contact-list__item {
    display: flex;
    align-items: flex-start;
    gap: 22px;
    margin-bottom: 20px;
    line-height: 26px;
  }
  .contact-list__icon {
    flex: none;
    width: 30px;
    height: 26px;
    fill: var(--ink-white);
  }
  .apply-link {
    position: absolute;
    left: 664px;
    top: 544px;
    margin: 0;
    font-size: 23px;
    font-weight: 700;
    white-space: nowrap;
  }
</style>
</head>
<body>
<div class="business-card">
  <svg class="card-background" viewBox="0 0 533 296" preserveAspectRatio="none" aria-hidden="true">
    <rect width="533" height="296" fill="var(--slate-dark)"/>
    <polygon points="0,0 250,0 0,200" fill="var(--slate-mid)" opacity="0.6"/>
    <polygon points="120,0 330,0 60,296 0,296 0,150" fill="var(--slate-mid)" opacity="0.45"/>
    <polygon points="130,296 533,30 533,70 200,296" fill="var(--slate-light)" opacity="0.55"/>
    <polygon points="420,0 533,0 533,98 262,140" fill="var(--accent-red)"/>
    <polygon points="480,0 533,0 533,98 430,114" fill="var(--accent-red-deep)" opacity="0.35"/>
    <polygon points="262,140 533,98 533,296 300,296 250,150" fill="var(--accent-blue)"/>
    <polygon points="420,122 533,104 533,296 360,296" fill="var(--accent-blue-deep)" opacity="0.4"/>
    <polygon points="533,262 533,296 488,296" fill="var(--accent-red)"/>
  </svg>

  <header class="identity">
    <h1 class="identity__name">Reid Calloway</h1>
    <p class="identity__credentials">
      Residential Mortgage Loan Originator NMLS 418273<br>
      Brightvale Home Loans NMLS 562091<br>
      Licensed in TX, AL, AR, CA, CO, FL, LA, OK
    </p>
    <p class="identity__promise">
      Top Producer 2013, 2014, 2015, 2016<br>
      Keeping the process simple and easy!
    </p>
  </header>

  <ul class="contact-list">
    <li class="contact-list__item">
      <svg class="contact-list__icon" viewBox="0 0 30 26" aria-label="Address"><path d="M15 1 1 13h4v12h7v-8h6v8h7V13h4z"/></svg>
      <span>2380 Marlow Creek Dr, Suite B<br>Houston, TX 77055</span>
    </li>
    <li class="contact-list__item">
      <svg class="contact-list__icon" viewBox="0 0 30 26" aria-label="Phone"><path d="M7 2c1-1 2-1 3 0l3 4c1 1 0 2-1 3l-1 1c1 3 3 5 6 6l1-1c1-1 2-2 3-1l4 3c1 1 1 2 0 3l-2 2c-2 2-8 0-12-4S5 6 5 4z"/></svg>
      <span>713.555.0182</span>
    </li>
    <li class="contact-list__item">
      <svg class="contact-list__icon" viewBox="0 0 30 26" aria-label="Fax"><path d="M8 2h11l3 3v5H8z M4 11h22a2 2 0 0 1 2 2v10a2 2 0 0 1-2 2H4a2 2 0 0 1-2-2V13a2 2 0 0 1 2-2z"/><rect x="9" y="15" width="12" height="2" fill="var(--accent-blue)"/><rect x="9" y="19" width="12" height="2" fill="var(--accent-blue)"/></svg>
      <span>281.555.0146</span>
    </li>
    <li class="contact-list__item">
      <svg class="contact-list__icon" viewBox="0 0 30 26" aria-label="Email"><path d="M2 5h26v16H2z"/><path d="M2 5l13 10L28 5" fill="none" stroke="var(--accent-blue)" stroke-width="2"/></svg>
      <span>teamreid@brightvalehomeloans.com</span>
    </li>
  </ul>

  <p class="apply-link">To Apply: https://teamreid.applyhub.com</p>
</div>
</body>
</html>
```